Ledgerwise Reach - B2B Demand Generation Website Project

We need a fully functional website for www.ledgerwisereach.example. We are a B2B Demand Generation company, based in London, working with companies such as QRT, VKD, Norvex, Brindlow, Tarvo generating them sales leads for their sales teams. We run this through digital marketing newsletter promotions and have a network of websites. Content syndication, data, demand generation, online marketing. Our logo has just been redone (attached) and we have a holding page already which i would like to use the style / colours. Our logo is bright and vibrant but i dont want the site to be a rainbow. We are expensive, classy, professorial, B2B, intelligent.

Home
About Us
Our Services
Prospora & QA Technology
Intent Data
Testimonials
Contact Us
Updates

Target Market(s)

B2B Marketers (QRT, Velquarion, Tarvo, VKD, Opal Reach, Driftmoor, Harlow Quantis, Technology Companies, Data Companies, Marketing Teams, Tumbleden.

Industry/Entity Type

Marketing

Coding

Coded - Design and coding required

Number of Pages Required

5+ page

Font styles to use
Sans Serif

Requirements
Must have
• Home
About Us
Our Services
Prospora & QA Technology
Intent Data
Testimonials
Contact Us

Simple Pages.

Look classy, intelligent, data experts. I like the video homepages were the image moves at the top. Very soft animation.
Nice to have
• Websites i like:

https://www.vkd.example/
https://www.brevantor.example/
https://www.plumfieldsites.example.co.uk/

Ledgerwise Reach - The Demand Generation Company
Should not have
• Glimpsevault crap images

```html
<!DOCTYPE html>
<html lang="en">
<head>
<meta charset="utf-8">
<title>Ledgerwise Reach - The Demand Generation Company</title>
<link rel="stylesheet" href="https://fonts.googleapis.com/css2?family=Roboto:wght@300;400;500;700&display=swap">
<style>
:root{
  --blue:#1b5ca6;
  --blue-dark:#0c3a74;
  --navy:#0a2a55;
  --red:#d3252c;
  --ink:#2b2b2b;
  --muted:#7a7a7a;
  --line:#e6e6e6;
  --footer:#262626;
}
*{box-sizing:border-box;margin:0;padding:0}
html,body{width:1200px;height:4637px;overflow:hidden}
body{position:relative;font-family:'Roboto',sans-serif;color:var(--ink);background:#fff}
.abs{position:absolute}
.btn{position:absolute;display:flex;align-items:center;justify-content:center;background:var(--red);color:#fff;font-size:11px;font-weight:500;border-radius:20px}
.dot{display:inline-block;border-radius:50%}

/* top bar */
.topbar{top:0;left:0;width:1200px;height:32px;font-size:10px;color:#8a8a8a}
.topbar span{position:absolute;top:10px}
.topbar .social{width:9px;height:9px;background:var(--blue);top:11px}
/* header */
.brand{display:flex;align-items:center;gap:8px;color:var(--red);font-size:17px;font-weight:400;white-space:nowrap}
.brand .mark{width:12px;height:12px;background:var(--blue);flex:none}
.feature{position:absolute;top:50px;display:flex;gap:10px;align-items:center;font-size:10px;color:#555;line-height:1.25}
.feature svg{width:18px;height:18px}
.navbar{top:94px;left:230px;width:735px;height:46px;background:var(--blue);z-index:3;display:flex;align-items:center;padding-left:22px;gap:18px;color:#fff;font-size:11px}
.navbar .active{border-bottom:3px solid var(--red);padding:15px 0 12px}
/* hero */
.hero{top:117px;left:0;width:1200px;height:558px;background:linear-gradient(180deg,#3a4756 0%,#2b3440 55%,#4e5a66 100%)}
.hero-copy{top:270px;width:1200px;text-align:center;color:#fff}
.hero-copy .kicker{font-size:10px;font-weight:500;letter-spacing:.3px}
.hero-copy h1{font-weight:300;font-size:50px;margin-top:12px;line-height:1.1}
.hero-copy h1 b{font-weight:700;display:block}
/* service cards */
.svc{top:589px;width:232px;height:221px;background:#fff;border:1px solid var(--line);text-align:center;padding-top:24px}
.svc .ic{width:48px;height:48px;margin:0 auto;border-radius:50%;background:#f2b7b7;border:4px solid #fbe4e4}
.svc h3{color:var(--blue);font-weight:400;font-size:15px;margin-top:14px;line-height:1.5}
.svc p{font-size:9.5px;color:var(--muted);margin:10px 22px 0;line-height:1.6}
.svc a{display:block;color:var(--red);font-size:9.5px;margin-top:16px}
.svc.on{background:linear-gradient(160deg,#3a70b3,#1d5196);border-color:transparent;border-bottom:3px solid var(--red)}
.svc.on .ic{background:rgba(255,255,255,.25);border-color:rgba(255,255,255,.15)}
.svc.on h3,.svc.on p,.svc.on a{color:#fff}
/* intro */
.label{font-size:9px;color:#aaa;letter-spacing:.3px}
.h2{color:var(--blue);font-weight:300;font-size:29px;line-height:1.1}
.h2 b{font-weight:700}
.contact-chip{top:1166px;width:173px;height:52px;border:1px solid var(--line);display:flex;align-items:center;gap:10px;padding-left:14px;font-size:9px;color:#555}
.contact-chip .c{width:26px;height:26px;border-radius:50%;background:var(--red);flex:none}
.contact-chip a{color:var(--red);text-decoration:underline;display:block;margin-top:2px}
/* stats */
.stats{top:1384px;left:0;width:1200px;height:187px;background:linear-gradient(135deg,#0c3770 0%,#1b5ca6 50%,#0d3a75 100%)}
.stat{top:1455px;width:250px;text-align:center;color:#fff}
.stat .n{font-size:25px;font-weight:500}
.stat .t{font-size:11px;margin-top:10px;font-weight:500}
/* mql boxes */
.box{top:1800px;width:231px;height:120px;border:1px solid var(--line);padding:16px 20px 0 62px;font-size:9.5px;color:var(--muted);line-height:1.6}
.box h4{color:var(--blue);font-weight:400;font-size:14px;line-height:1.1;margin-bottom:10px}
.box svg{position:absolute;left:20px;top:18px;width:28px;height:28px}
.box.on{background:linear-gradient(160deg,#3a70b3,#1d5196);color:#fff;border:none;border-bottom:3px solid var(--red)}
.box.on h4{color:#fff}
/* photo band */
.band{top:2023px;left:0;width:1200px;height:312px;background:linear-gradient(110deg,#06233f 0%,#0b4a8a 45%,#1b6bb8 70%,#0b2f5c 100%)}
.whatcard{top:2178px;left:234px;width:356px;height:283px;background:#fff;box-shadow:0 2px 14px rgba(0,0,0,.12);padding:30px 30px}
.whatcard h4{color:var(--blue);font-weight:400;font-size:14px}
.whatcard p{font-size:9.5px;color:var(--muted);line-height:1.7;margin-top:22px}
.tick{position:absolute;display:flex;gap:10px;font-size:9.5px;color:#333;line-height:1.3;width:150px}
.tick i{flex:none;width:26px;height:26px;border-radius:50%;background:var(--red);display:flex;align-items:center;justify-content:center}
/* services */
.tabs{top:2630px;left:230px;width:735px;height:28px;border-bottom:1px solid var(--line);font-size:11px;color:var(--blue)}
.tabs span{position:absolute;top:4px}
.svc-text{top:2696px;left:230px;width:735px;text-align:center;font-size:12px;line-height:1.55;color:#333}
.svc-text p{margin-bottom:18px}
/* contact band */
.cta{top:2999px;left:0;width:1200px;height:288px;background:linear-gradient(135deg,#0d3b76 0%,#1b5ca6 55%,#134b8f 100%);text-align:center;color:#fff}
/* testimonials */
.tcard{top:3532px;width:234px;height:257px;background:#fff;box-shadow:0 2px 12px rgba(0,0,0,.08);text-align:center;padding-top:26px}
.tcard .av{width:62px;height:62px;border-radius:50%;background:#7f7f7f;margin:0 auto}
.tcard h5{font-weight:400;font-size:12px;margin-top:18px}
.tcard .role{color:var(--red);font-size:9px;margin-top:4px}
.tcard p{font-size:9.5px;color:var(--muted);line-height:1.6;margin:20px 24px 0}
.tcard.on{border-bottom:4px solid var(--red)}
/* touch */
.touch-bg{top:3861px;left:0;width:1200px;height:504px;background:linear-gradient(120deg,#1d2a39 0%,#34414f 45%,#1c2836 100%)}
.touch-panel{top:3924px;left:230px;width:337px;height:428px;background:rgba(18,72,140,.93);color:#fff;padding:34px 42px}
.touch-panel h2{font-weight:400;font-size:30px;line-height:1}
.touch-panel h2 b{font-weight:500}
.touch-panel .intro{font-size:9.5px;line-height:1.6;margin-top:12px}
.tp{position:absolute;font-size:9px;line-height:1.6;width:124px}
.tp b{font-weight:500}
.tp em{font-style:normal;color:#ffb4b4}
.form{top:3924px;left:630px;width:335px;height:428px;background:#fff;padding:46px 22px;text-align:center}
.form h4{color:var(--blue);font-weight:400;font-size:14px}
.form p{font-size:9.5px;color:var(--muted);margin-top:12px;line-height:1.6}
.field{border:1px solid var(--line);height:28px;text-align:left;font-size:9.5px;color:#999;padding:8px 10px;margin-top:12px}
/* footer */
.footer{top:4365px;left:0;width:1200px;height:272px;background:var(--footer);color:#bbb}
.fcol{position:absolute;top:58px;font-size:9.5px;line-height:1.9}
.fcol h6{color:#fff;font-size:11px;font-weight:500;margin-bottom:14px}
</style>
</head>
<body>

<!-- top bar -->
<div class="abs topbar">
  <span style="left:200px;color:var(--red)">&#9993;</span>
  <span style="left:216px">info@ledgerwisereach.example</span>
  <span style="left:364px;color:var(--red)">&#9679;</span>
  <span style="left:377px">48 Halden Row, London</span>
  <span style="left:748px;color:#444">Careers</span>
  <span style="left:796px">Help Desk</span>
  <i class="abs social dot" style="left:893px"></i>
  <i class="abs social dot" style="left:913px"></i>
  <i class="abs social dot" style="left:933px"></i>
  <i class="abs social dot" style="left:953px;background:#ccc"></i>
</div>

<!-- header -->
<div class="abs brand" style="top:46px;left:244px"><i class="mark"></i>Ledgerwise Reach</div>
<div class="feature" style="left:436px"><svg viewBox="0 0 20 20"><rect x="2" y="2" width="16" height="16" rx="2" fill="none" stroke="#d3252c" stroke-width="1.6"/><path d="M6 10l3 3 5-6" fill="none" stroke="#d3252c" stroke-width="1.6"/></svg><span>Guaranteed<br>Results</span></div>
<div class="feature" style="left:553px"><svg viewBox="0 0 20 20"><circle cx="10" cy="10" r="8" fill="none" stroke="#d3252c" stroke-width="1.6"/><path d="M10 5v5l3 2" fill="none" stroke="#d3252c" stroke-width="1.6"/></svg><span>24/7<br>Service</span></div>
<div class="feature" style="left:670px"><svg viewBox="0 0 20 20"><path d="M3 9h4v9H3zM7 9l4-7c2 0 2 2 1.5 5H17l-1.5 11H7" fill="none" stroke="#d3252c" stroke-width="1.6"/></svg><span>Qualified<br>Professionals</span></div>
<div class="feature" style="left:834px;top:48px"><svg viewBox="0 0 20 20"><path d="M5 2l3 4-2 2c1 3 3 5 6 6l2-2 4 3-2 3C9 18 2 11 2 4z" fill="#d3252c"/></svg><span style="color:var(--blue)">Office Line<br><b style="color:var(--red);font-weight:500">(+44) 20 7946 0182</b></span></div>

<!-- hero -->
<div class="abs hero" role="img" aria-label="Photo of a professional working on a laptop on a leather sofa, dark blue-grey tones"></div>
<nav class="abs navbar">
  <span class="active">Home &#9662;</span><span>About Us</span><span>Services</span><span>QA Technology</span><span>Intent Data</span><span>Contact</span>
  <span class="btn" style="right:20px;top:10px;width:112px;height:27px;position:absolute">Get A Quote</span>
</nav>
<div class="abs hero-copy">
  <div class="kicker">MULTI-CHANNEL DEMAND GENERATION SERVICES</div>
  <h1>We can assist you in delivering your<b>demand generation strategy</b></h1>
</div>
<div class="btn" style="top:439px;left:545px;width:110px;height:27px">About Us</div>

<!-- service cards -->
<div class="abs svc" style="left:230px"><div class="ic"></div><h3>Marketing Qualified<br>Leads</h3><p>This is a prospect that has expressed an interest in what your brand has to offer.</p><a>Read More</a></div>
<div class="abs svc on" style="left:481px"><div class="ic"></div><h3>Accounting Based<br>Marketing Leads</h3><p>This is a strategy that directs marketing to a specific set of target accounts</p><a>Read More</a></div>
<div class="abs svc" style="left:729px"><div class="ic"></div><h3>Sales Qualified<br>Leads</h3><p>This is a lead that expressed a specific interest in a product/service that you offer</p><a>Read More</a></div>

<!-- intro -->
<div class="abs label" style="top:901px;left:234px">WELCOME TO LEDGERWISE REACH</div>
<h2 class="abs h2" style="top:926px;left:234px">We deliver high quality<br><b>sales leads</b></h2>
<p class="abs" style="top:1011px;left:234px;width:330px;font-size:11.5px;line-height:1.65">This can include leads via email or telemarketing, account-based targeting (ABM) or identifying need and pain points through BANT / SQL campaigns.</p>
<p class="abs" style="top:1088px;left:234px;width:330px;font-size:9.5px;line-height:1.7;color:var(--muted)">Ledgerwise Reach offer expert demand generation support, from providing detailed leads of qualified decision-makers, to a comprehensive lead generation and SQL service.</p>
<div class="abs contact-chip" style="left:232px"><i class="c"></i><div>Contact Us<a>+44 20 7946 0182</a></div></div>
<div class="abs contact-chip" style="left:420px"><i class="c"></i><div>Our Email<a>info@ledgerwisereach</a></div></div>
<div class="btn" style="top:1251px;left:232px;width:114px;height:27px">Read More</div>
<div class="abs" style="top:870px;left:608px;width:357px;height:411px;background:linear-gradient(160deg,#e8eef3,#b9c7d6 55%,#8ea2b8)" role="img" aria-label="Photo of a smiling businessman in a light blue blazer talking on the phone"></div>

<!-- stats -->
<div class="abs stats" role="img" aria-label="Dark blue background with a faint network of connected points"></div>
<div class="abs stat" style="left:192px"><div class="n">70,000+</div><div class="t">Downloads Per Month</div></div>
<div class="abs stat" style="left:494px"><div class="n">25,000+</div><div class="t">Leads Delivered Per Month</div></div>
<div class="abs stat" style="left:746px"><div class="n">50+</div><div class="t">Countries We Can</div></div>
<div class="abs" style="top:1442px;left:453px;width:1px;height:64px;background:rgba(255,255,255,.3)"></div>
<div class="abs" style="top:1442px;left:765px;width:1px;height:64px;background:rgba(255,255,255,.3)"></div>

<!-- about -->
<div class="abs label" style="top:1636px;left:230px">ABOUT US</div>
<h2 class="abs h2" style="top:1660px;left:230px">Whether looking for<br><b>MQL, ABM or BANT</b><br>campaigns.</h2>
<p class="abs" style="top:1664px;left:605px;width:330px;font-size:11.5px;line-height:1.65">With access to over 31 million names, Ledgerwise Reach offers a range of marketing options that allow you to use our data to target the decision makers you need to reach.</p>
<div class="abs box" style="left:230px"><svg viewBox="0 0 20 20"><rect x="2" y="2" width="16" height="16" rx="2" fill="none" stroke="#d3252c" stroke-width="1.4"/><path d="M6 10l3 3 5-6" fill="none" stroke="#d3252c" stroke-width="1.4"/></svg><h4>Guaranteed<br>Results</h4>Lorem ipsum dolor sit amet, consectetur adipiscing elit, sed do eiusmod tempor incididunt.</div>
<div class="abs box" style="left:480px"><svg viewBox="0 0 20 20"><circle cx="10" cy="10" r="8" fill="none" stroke="#d3252c" stroke-width="1.4"/><path d="M10 5v5l3 2" fill="none" stroke="#d3252c" stroke-width="1.4"/></svg><h4>24/7<br>Service</h4>Lorem ipsum dolor sit amet, consectetur adipiscing elit, sed do eiusmod tempor incididunt.</div>
<div class="abs box on" style="left:729px"><svg viewBox="0 0 20 20"><path d="M3 9h4v9H3zM7 9l4-7c2 0 2 2 1.5 5H17l-1.5 11H7" fill="none" stroke="#fff" stroke-width="1.4"/></svg><h4>Qualified<br>Professionals</h4>Lorem ipsum dolor sit amet, consectetur adipiscing elit, sed do eiusmod tempor incididunt.</div>

<!-- what we do -->
<div class="abs band" role="img" aria-label="Abstract blue technology image with glowing light dots"></div>
<div class="abs whatcard">
  <h4>What we Do</h4>
  <p>Our extensive and ongoing research campaigns give you the ability to build contact lists that identify individuals at all stages of the buying cycle, from pre-sales to sales ready.</p>
</div>
<div class="tick" style="top:2324px;left:264px"><i><svg width="12" height="12" viewBox="0 0 12 12"><path d="M2 6l3 3 5-6" fill="none" stroke="#fff" stroke-width="1.8"/></svg></i><span>Breakdown by geography, job title, role and responsibility</span></div>
<div class="tick" style="top:2324px;left:425px"><i><svg width="12" height="12" viewBox="0 0 12 12"><path d="M2 6l3 3 5-6" fill="none" stroke="#fff" stroke-width="1.8"/></svg></i><span>Targeting through previous research and buying intention</span></div>
<div class="tick" style="top:2386px;left:264px"><i><svg width="12" height="12" viewBox="0 0 12 12"><path d="M2 6l3 3 5-6" fill="none" stroke="#fff" stroke-width="1.8"/></svg></i><span>Email dispatch to selected individuals</span></div>
<div class="tick" style="top:2386px;left:425px"><i><svg width="12" height="12" viewBox="0 0 12 12"><path d="M2 6l3 3 5-6" fill="none" stroke="#fff" stroke-width="1.8"/></svg></i><span>Extensive telemarketing options</span></div>

<!-- services -->
<h2 class="abs h2" style="top:2514px;width:1200px;text-align:center">Our <b style="font-weight:500">Services</b></h2>
<div class="abs tabs">
  <span style="left:3px">Marketing Qualified Leads (MQL)</span>
  <span style="left:250px">Account Based Marketing Leads (ABM)</span>
  <span style="right:18px">Sales Qualified Lead / BANT</span>
  <i class="abs" style="left:0;bottom:-1px;width:190px;height:2px;background:var(--blue)"></i>
</div>
<div class="abs svc-text">
  <p>A Marketing Qualified Lead (MQL) is a prospect that has expressed an interest in what your brand has to offer.<br>An MQL has taken the first steps to becoming a customer and is ready to receive additional content from your company.<br>From a very general perspective: Marketing Qualified Leads turn into Sales Qualified Leads (SQLs), which in<br>turn can convert into customers once they have been through the buyer's journey.</p>
  <p>It's important for each potential customer to travel through all stages of the buying journey and the MQL is the first step in<br>this process. This engagement warms them up to your brand, builds trust and puts them in the position to consider your solution<br>as the right fit for their business.</p>
  <p>The MQL is the foundation of a B2B demand generation strategy and helps businesses identify<br>those prospects who could be in the market for their services.</p>
</div>

<!-- contact band -->
<div class="abs cta" role="img" aria-label="Blue background with faint financial chart lines and figures"></div>
<div class="abs" style="top:3052px;width:1200px;text-align:center;color:#fff">
  <div style="font-size:28px;font-weight:300">Contact Us for <b style="font-weight:500">more info</b></div>
  <p style="font-size:11px;line-height:1.7;width:560px;margin:16px auto 0;color:#cfe0f3">Lorem ipsum dolor sit amet, consectetur adipiscing elit, sed do eiusmod tempor incididunt ut labore et dolore magna aliqua. Ut enim ad minim veniam, quis nostrud exercitation ullamco</p>
</div>
<div class="btn" style="top:3196px;left:545px;width:110px;height:26px">Get A Quote</div>

<!-- testimonials -->
<div class="abs label" style="top:3348px;width:1200px;text-align:center;color:#555">TESTIMONIALS</div>
<h2 class="abs h2" style="top:3372px;width:1200px;text-align:center">What Our Clients Say<br><b style="font-weight:500">About Us</b></h2>
<p class="abs" style="top:3458px;left:320px;width:560px;text-align:center;font-size:11.5px;line-height:1.6">Lorem ipsum dolor sit amet, consectetur adipiscing elit, sed do eiusmod tempor incididunt ut labore et dolore magna aliqua. Ut enim ad minim veniam, quis nostrud</p>
<div class="abs tcard" style="left:225px"><div class="av"></div><h5>Maren Holt</h5><div class="role">Industrial Engineer and CEO</div><p>Lorem ipsum dolor sit amet, consectetur adipiscing elit, sed do eiusmod tempor incididunt ut labore et dolore magna aliqua. Ut enim</p></div>
<div class="abs tcard on" style="left:475px"><div class="av"></div><h5>Maren Holt</h5><div class="role">Industrial Engineer and CEO</div><p>Lorem ipsum dolor sit amet, consectetur adipiscing elit, sed do eiusmod tempor incididunt ut labore et dolore magna aliqua. Ut enim</p></div>
<div class="abs tcard" style="left:724px"><div class="av"></div><h5>Maren Holt</h5><div class="role">Industrial Engineer and CEO</div><p>Lorem ipsum dolor sit amet, consectetur adipiscing elit, sed do eiusmod tempor incididunt ut labore et dolore magna aliqua. Ut enim</p></div>
<i class="abs dot" style="top:3822px;left:570px;width:8px;height:8px;border:1.5px solid var(--red)"></i>
<i class="abs" style="top:3825px;left:584px;width:18px;height:2px;background:var(--red)"></i>
<i class="abs dot" style="top:3822px;left:607px;width:8px;height:8px;border:1.5px solid var(--red)"></i>

<!-- get in touch -->
<div class="abs touch-bg" role="img" aria-label="Dark photo of hands holding a smartphone"></div>
<div class="abs touch-panel">
  <h2>Get in <b>Touch</b></h2>
  <p class="intro">Lorem ipsum dolor sit amet, consectetur adipiscing elit, sed do eiusmod tempor incididunt ut labore et dolore magna aliqua. Ut enim ad minim veniam, quis nostrud</p>
</div>
<div class="tp" style="top:4062px;left:272px;color:#fff"><b>Ledgerwise Reach</b><br>48 Halden Row, London<br><em>&#9679; Find Us on Map</em></div>
<div class="tp" style="top:4062px;left:398px;color:#fff"><b>Ledgerwise Reach</b><br>48 Halden Row, London<br><em>&#9679; Find Us on Map</em></div>
<div class="tp" style="top:4124px;left:272px;color:#fff"><b>Ledgerwise Reach</b><br>&#9742; +44 20 7946 0182</div>
<div class="tp" style="top:4124px;left:398px;color:#fff"><b>Ledgerwise Reach</b><br>&#9742; +44 20 7946 0182</div>
<div class="tp" style="top:4170px;left:272px;color:#fff"><b>Ledgerwise Reach</b><br>&#9742; +44 20 7946 0182</div>
<div class="tp" style="top:4170px;left:398px;color:#fff"><b>Ledgerwise Reach</b><br>&#9742; +44 20 7946 0182</div>
<div class="tp" style="top:4216px;left:272px;color:#fff;width:200px"><b>Ledgerwise Reach</b><br><em>&#9993; info@ledgerwisereach.example</em></div>
<div class="abs form">
  <h4>Let's Talk About Your Project</h4>
  <p>After we get some information from you, we'll set up<br>a time to discuss your project in further detail.</p>
  <div class="field" style="margin-top:22px">Name</div>
  <div class="field">Email</div>
  <div class="field" style="height:92px">Message</div>
</div>
<div class="btn" style="top:4237px;left:741px;width:112px;height:26px">Submit</div>

<!-- footer -->
<footer class="abs footer">
  <div class="abs brand" style="top:46px;left:230px;font-size:15px"><i class="mark" style="width:11px;height:11px"></i>Ledgerwise Reach</div>
  <p class="abs" style="top:84px;left:230px;width:170px;font-size:9.5px;line-height:1.7;color:#ddd">Lorem ipsum dolor sit amet, consec tetur adipiscing elit, sed do eiusmod tempor incididunt ut labore et dolore magna aliqua. Ut enim</p>
  <i class="abs dot" style="top:167px;left:231px;width:7px;height:7px;background:#aaa"></i>
  <i class="abs dot" style="top:167px;left:251px;width:7px;height:7px;background:#aaa"></i>
  <i class="abs dot" style="top:167px;left:272px;width:7px;height:7px;background:#aaa"></i>
  <i class="abs dot" style="top:167px;left:293px;width:7px;height:7px;background:#aaa"></i>
  <div class="fcol" style="left:421px"><h6>Useful Links</h6>About Us<br>Testimonials<br>Services<br>Home</div>
  <div class="fcol" style="left:505px"><h6>&nbsp;</h6>Intent Data<br>QA Technology</div>
  <div class="fcol" style="left:608px;color:#fff"><h6>Contacts</h6><span style="color:var(--red)">&#9679;</span> 24/7<br><span style="color:var(--red)">&#9679;</span> 48 Halden Row, London<br><span style="color:var(--red)">&#9742;</span> (+44) 20 7946 0182<br><span style="color:var(--red)">&#9993;</span> info@ledgerwisereach.example</div>
  <div class="fcol" style="left:796px"><h6>Newsletter</h6></div>
  <div class="abs" style="top:92px;left:796px;width:170px;height:26px;border-radius:14px;background:#3a3a3a;font-size:9px;color:#999;padding:7px 14px">Your email...</div>
  <div class="abs" style="top:128px;left:796px;width:116px;height:26px;border-radius:14px;border:1px solid var(--red);color:var(--red);font-size:9.5px;text-align:center;padding-top:6px">Subscribe</div>
</footer>

</body>
</html>
```